Refresh Application User Interface

Brindlecove wishes to update the look of its business applications. Two representative forms are shown below. Please note, we are not considering changes in functionality or usability. Our goal is a cleaner, more contemporary design.

Industry/Entity Type

Business

```html
<!DOCTYPE html>
<html lang="en">
<head>
<meta charset="utf-8">
<title>Brindlecove – Purchase Order</title>
<link rel="stylesheet" href="https://fonts.googleapis.com/css2?family=Montserrat:wght@400;500;600;700&display=swap">
<style>
:root{
  --topbar:#3a3a3c;
  --topbar-active:#4b4b4e;
  --blue:#0a4d9c;
  --blue-active:#2c64ad;
  --green:#84c441;
  --green-text:#7ab83a;
  --ink:#333;
  --panel:#f4f4f4;
  --border:#dcdcdc;
  --white:#fff;
}
*{box-sizing:border-box;margin:0;padding:0}
html,body{width:1200px;height:1116px;overflow:hidden;background:var(--white)}
body{font-family:"Montserrat",sans-serif;color:var(--ink);position:relative;font-size:14px}
.abs{position:absolute}
svg{display:block}

/* top bar */
.topbar{left:0;top:0;width:1200px;height:36px;background:var(--topbar);color:#eee;font-size:13.5px}
.topbar .status{top:0;height:36px;display:flex;align-items:center;gap:6px;white-space:nowrap}
.topbar .status b{font-weight:600;margin-left:-2px}
.dot{flex:none;width:14px;height:14px;border-radius:50%;border:2px solid #eee;display:flex;align-items:center;justify-content:center}
.dot::after{content:"";width:6px;height:6px;border-radius:50%;background:var(--green)}
.dot.role::after{background:#eee}
.util{top:0;height:36px;display:flex;align-items:center;justify-content:center;gap:6px;border-left:1px solid #555;white-space:nowrap}
.util.active{background:var(--topbar-active)}

/* main nav */
.nav a{position:absolute;top:52px;font-size:16.5px;font-weight:500;color:#3a3a3a;text-decoration:none}
.nav a.current{color:var(--green-text)}
.nav .home-line{left:29px;top:93px;width:47px;height:2px;background:#333}
.brand{right:30px;top:46px;font-size:34px;font-weight:700;color:var(--blue);letter-spacing:-.5px}

/* sub nav */
.subnav{left:0;top:95px;width:1200px;height:48px;background:var(--green)}
.subnav a{position:absolute;top:15px;font-size:14.5px;color:var(--white);text-decoration:none}
.subnav a.current{color:#2a2a2a}
.subnav .current-line{left:29px;top:46px;width:47px;height:2px;background:#333}

/* page header */
.page-title{left:28px;top:183px;font-size:23px;font-weight:500;color:#2f2f2f}
.doc-tab{top:173px;height:48px;display:flex;align-items:center;justify-content:center;font-size:16.5px;font-weight:500;color:#444;border:1px solid var(--border);border-left:none;background:var(--white)}
.doc-tab.active{background:var(--blue);color:var(--white);border-color:var(--blue)}

/* toolbar */
.toolbar{left:30px;top:221px;width:1140px;height:36px;background:var(--blue)}
.tool{top:0;height:36px;display:flex;align-items:center;justify-content:center;gap:7px;color:var(--white);font-size:13.5px;border-right:1px solid #2b60a6;white-space:nowrap}
.tool.active{background:var(--blue-active)}

/* body */
.frame{left:30px;top:257px;width:1140px;height:825px;border:1px solid var(--border);border-top:none}
.panel{left:66px;top:294px;width:1068px;height:749px;background:var(--panel)}
.lbl{font-size:14.5px;color:#3a3a3a;white-space:nowrap}
.lbl.r{text-align:right}
.field{height:34px;background:var(--white);border:1px solid var(--border);border-radius:3px;display:flex;align-items:center;padding:0 11px;font-size:14.5px;color:#333;white-space:nowrap;overflow:hidden}
.field.select{justify-content:space-between}
.chev{width:10px;height:6px;flex:none}
.link{font-size:14.5px;font-weight:600;color:var(--blue);text-decoration:underline}
.order-kind{right:107px;top:331px;font-size:14.5px;font-weight:600;color:var(--green-text)}
.order-kind span{color:var(--blue)}

/* section tabs */
.sec-tab{top:639px;height:49px;display:flex;align-items:center;justify-content:center;background:var(--blue);color:var(--white);font-size:16.5px;font-weight:600;border-right:1px solid #2b60a6}
.sec-tab.active{background:var(--white);color:#333;font-weight:500;border:1px solid var(--border);border-bottom:none}
.sec-body{left:106px;top:688px;width:987px;height:288px;background:var(--white);border:1px solid var(--border)}
.lock{left:1040px;top:925px;width:53px;height:51px;border-left:1px solid var(--border);border-top:1px solid var(--border);background:var(--panel);display:flex;align-items:center;justify-content:center}
.hint{left:0;width:1200px;top:996px;text-align:center;font-size:14px;color:#333;font-weight:500}
</style>
</head>
<body>

<!-- top bar -->
<div class="abs topbar">
  <div class="abs status" style="left:15px"><span class="dot"></span>Logged in as <b>Dana Whitfield</b></div>
  <div class="abs status" style="left:252px"><span class="dot role"></span>Current Role <b>Administrator</b></div>
  <div class="abs util active" style="left:745px;width:85px;border-left:none">
    <svg width="14" height="12" viewBox="0 0 14 12" fill="none" stroke="#eee" stroke-width="1.4"><path d="M4 2h10M4 6h10M4 10h10M0 2h2M0 6h2M0 10h2"/></svg>Touch</div>
  <div class="abs util" style="left:830px;width:100px">
    <svg width="13" height="13" viewBox="0 0 13 13" fill="none" stroke="#eee" stroke-width="1.3"><rect x="1" y="1" width="11" height="11"/><path d="M1 4h11M6.5 6v5M4 8.5h5"/></svg>New Tab</div>
  <div class="abs util" style="left:930px;width:74px">
    <svg width="14" height="14" viewBox="0 0 14 14" fill="none" stroke="#eee" stroke-width="1.3"><circle cx="7" cy="7" r="6"/><path d="M5.2 5.3a1.9 1.9 0 1 1 2.5 1.8c-.5.2-.7.6-.7 1.2M7 10.2v.2"/></svg>Help</div>
  <div class="abs util" style="left:1004px;width:99px">
    <svg width="14" height="14" viewBox="0 0 14 14" fill="none" stroke="#eee" stroke-width="1.3"><path d="M2 12L12 2M2 2l10 10M1 1l3 1-1 1zM13 13l-3-1 1-1z"/></svg>Support</div>
  <div class="abs util" style="left:1103px;width:97px">
    <svg width="13" height="14" viewBox="0 0 13 14" fill="none" stroke="#eee" stroke-width="1.3"><path d="M8 4V1H1v12h7v-3M5 7h8M10.5 4.5L13 7l-2.5 2.5"/></svg>Log Out</div>
</div>

<!-- main navigation -->
<nav class="nav">
  <a style="left:29px">Home</a>
  <a style="left:108px">eSource</a>
  <a style="left:204px" class="current">eBuy</a>
  <svg class="abs" style="left:219px;top:80px" width="10" height="6" viewBox="0 0 10 6" fill="none" stroke="#84c441" stroke-width="1.4"><path d="M1 1l4 4 4-4"/></svg>
  <a style="left:276px">eRequest</a>
  <a style="left:383px">eSell</a>
  <a style="left:452px">eStock</a>
  <a style="left:537px">ePlan</a>
  <a style="left:614px">Preference</a>
  <div class="abs home-line"></div>
</nav>
<div class="abs brand">Brindlecove</div>

<!-- sub navigation -->
<div class="abs subnav">
  <a style="left:29px" class="current">Orders</a>
  <a style="left:98px">Receipts</a>
  <a style="left:179px">Shipment</a>
  <a style="left:270px">Invoices</a>
  <a style="left:348px">Pricing</a>
  <a style="left:418px">Tables</a>
  <a style="left:485px">Reports</a>
  <a style="left:560px">Inquiries</a>
  <a style="left:643px">Periodic Tasks</a>
  <a style="left:762px">Workflows</a>
  <div class="abs current-line"></div>
</div>

<!-- page header -->
<h1 class="abs page-title">Purchase Order</h1>
<div class="abs doc-tab active" style="left:822px;width:91px">Header</div>
<div class="abs doc-tab" style="left:913px;width:77px">Lines</div>
<div class="abs doc-tab" style="left:990px;width:103px">Charges</div>
<div class="abs doc-tab" style="left:1093px;width:77px">Notes</div>

<!-- toolbar -->
<div class="abs toolbar">
  <div class="abs tool active" style="left:0;width:39px">
    <svg width="16" height="16" viewBox="0 0 16 16" fill="none" stroke="#fff" stroke-width="1.3"><path d="M13 7l-5.5 5.5a3 3 0 0 1-4.2-4.2L9 2.6a2 2 0 0 1 2.8 2.8L6.3 11a1 1 0 0 1-1.4-1.4L10 4.5"/></svg></div>
  <div class="abs tool" style="left:39px;width:38px">
    <svg width="16" height="17" viewBox="0 0 16 17" fill="none" stroke="#fff" stroke-width="1.3"><path d="M10 1H2v15h10M10 1l3 3v3M10 1v3h3M4 6h4M4 9h3M4 12h3"/><circle cx="11" cy="11" r="2.3"/><path d="M12.7 12.7l2.3 2.3"/></svg></div>
  <div class="abs tool" style="left:77px;width:39px">
    <svg width="18" height="16" viewBox="0 0 18 16" fill="none" stroke="#fff" stroke-width="1.3"><circle cx="3" cy="3" r="2"/><circle cx="15" cy="3" r="2"/><circle cx="9" cy="13" r="2"/><path d="M5 3h8M4 5l4 6.5M14 5l-4 6.5"/></svg></div>
  <div class="abs tool" style="left:116px;width:39px">
    <svg width="17" height="16" viewBox="0 0 17 16" fill="none" stroke="#fff" stroke-width="1.3"><rect x="1" y="4" width="15" height="11"/><path d="M5 4V1h7v3M1 8h15M4 11h3M10 11h3"/></svg></div>
  <div class="abs tool" style="left:155px;width:38px">
    <svg width="17" height="17" viewBox="0 0 17 17" fill="none" stroke="#fff" stroke-width="1.3"><circle cx="8.5" cy="8.5" r="7.5"/><path d="M6.3 6.5a2.3 2.3 0 1 1 3 2.2c-.5.2-.8.7-.8 1.3M8.5 12.3v.3"/></svg></div>
  <div class="abs tool" style="left:193px;width:160px">
    <svg width="18" height="17" viewBox="0 0 18 17" fill="none" stroke="#fff" stroke-width="1.3"><path d="M2 15L15 2M2 2l13 13M1 1l4 1.5L3 4zM16 16l-4-1.5 2-1.5z"/></svg>View GL Accounts</div>
  <div class="abs tool" style="left:353px;width:114px">
    <svg width="16" height="12" viewBox="0 0 16 12" fill="none" stroke="#fff" stroke-width="1.4"><path d="M4 1h12M4 6h12M4 11h12M0 1h2M0 6h2M0 11h2"/></svg>Post Order</div>

  <div class="abs tool active" style="left:728px;width:88px;border-left:1px solid #2b60a6">
    <svg width="16" height="16" viewBox="0 0 16 16" fill="none" stroke="#fff" stroke-width="1.5"><circle cx="6.5" cy="6.5" r="5"/><path d="M10.3 10.3L15 15"/></svg>Search</div>
  <div class="abs tool" style="left:816px;width:75px">
    <svg width="16" height="16" viewBox="0 0 16 16" fill="none" stroke="#fff" stroke-width="1.3"><circle cx="8" cy="8" r="7"/><path d="M8 4v8M4 8h8"/></svg>New</div>
  <div class="abs tool" style="left:891px;width:82px">
    <svg width="16" height="12" viewBox="0 0 16 12" fill="none" stroke="#fff" stroke-width="1.6"><path d="M1 6l4.5 4.5L15 1"/></svg>Apply</div>
  <div class="abs tool" style="left:973px;width:88px">
    <svg width="14" height="16" viewBox="0 0 14 16" fill="none" stroke="#fff" stroke-width="1.3"><path d="M1 3h12M5 3V1h4v2M2.5 3l1 12h7l1-12M5.5 6v6.5M8.5 6v6.5"/></svg>Delete</div>
  <div class="abs tool" style="left:1061px;width:79px;border-right:none">
    <svg width="16" height="14" viewBox="0 0 16 14" fill="none" stroke="#fff" stroke-width="1.3"><path d="M6 1L1 6l5 5M1 6h8a6 6 0 0 1 6 6v1"/></svg>Back</div>
</div>

<div class="abs frame"></div>
<div class="abs panel"></div>

<!-- order details -->
<div class="abs lbl r" style="left:90px;width:84px;top:331px">Order #</div>
<div class="abs lbl" style="left:198px;top:331px">100159</div>
<div class="abs order-kind">Regular Purchase Order | <span>Hold For Completion</span></div>

<div class="abs lbl r" style="left:90px;width:84px;top:372px">Skip from</div>
<div class="abs field" style="left:198px;top:363px;width:159px">1001</div>
<div class="abs lbl" style="left:368px;top:370px;font-size:16px">/</div>
<div class="abs field" style="left:386px;top:363px;width:58px">0</div>

<div class="abs lbl r" style="left:90px;width:84px;top:414px">Address</div>
<div class="abs field" style="left:198px;top:406px;width:479px">Harborline Medical Co.</div>
<div class="abs field" style="left:198px;top:449px;width:479px">14 Tidewater Rd</div>
<svg class="abs" style="left:703px;top:410px" width="26" height="26" viewBox="0 0 26 26" aria-label="Validate address">
  <circle cx="13" cy="13" r="12" fill="#fff" stroke="#e2e2e2"/>
  <circle cx="13" cy="13" r="7.5" fill="#84c441"/>
  <path d="M9 9.5c1.5-.5 2.5.5 3 1.5s-1 2 0 3 1 2 .5 3M15 7.5c-.5 1.5.5 2.5 1.5 2.5s1.5 1.5 1 3" fill="none" stroke="#fff" stroke-width="1.2"/>
</svg>
<div class="abs link" style="left:702px;top:455px">DPV Unconfimed</div>

<div class="abs lbl r" style="left:90px;width:84px;top:500px">City</div>
<div class="abs field" style="left:198px;top:491px;width:173px">Westbrook</div>
<div class="abs lbl" style="left:420px;top:500px">State</div>
<div class="abs field" style="left:503px;top:491px;width:174px">MA</div>
<div class="abs" style="left:701px;top:500px;width:17px;height:17px;border:1px solid #d6d6d6;background:#fff;display:flex;align-items:center;justify-content:center">
  <svg width="10" height="8" viewBox="0 0 10 8" fill="none" stroke="#84c441" stroke-width="1.6"><path d="M1 4l2.8 2.8L9 1"/></svg>
</div>
<div class="abs lbl" style="left:724px;top:500px">Accept</div>

<div class="abs lbl r" style="left:90px;width:84px;top:542px">Zip</div>
<div class="abs field" style="left:198px;top:534px;width:173px">01942-3018</div>
<div class="abs lbl" style="left:420px;top:542px">Country</div>
<div class="abs field" style="left:503px;top:534px;width:174px">US</div>
<div class="abs link" style="left:702px;top:541px">Add Contact</div>

<!-- section tabs -->
<div class="abs sec-tab" style="left:106px;width:120px">Order Info</div>
<div class="abs sec-tab active" style="left:226px;width:106px">Shipping</div>
<div class="abs sec-tab" style="left:332px;width:118px">Payments</div>
<div class="abs sec-tab" style="left:450px;width:111px">Accounts</div>
<div class="abs sec-tab" style="left:561px;width:164px;border-right:none">Totals/Approval</div>
<div class="abs sec-body"></div>

<!-- shipping fields: left column -->
<div class="abs lbl r" style="left:110px;width:132px;top:713px">Receive At</div>
<div class="abs field select" style="left:262px;top:706px;width:160px">ALCH<svg class="chev" viewBox="0 0 10 6" fill="none" stroke="#0a4d9c" stroke-width="1.4"><path d="M1 1l4 4 4-4"/></svg></div>
<div class="abs lbl r" style="left:110px;width:132px;top:754px">Carrier</div>
<div class="abs field select" style="left:262px;top:747px;width:160px">Swiftline<svg class="chev" viewBox="0 0 10 6" fill="none" stroke="#0a4d9c" stroke-width="1.4"><path d="M1 1l4 4 4-4"/></svg></div>
<div class="abs lbl r" style="left:110px;width:132px;top:796px">Express Service</div>
<div class="abs field select" style="left:262px;top:788px;width:160px"><span></span><svg class="chev" viewBox="0 0 10 6" fill="none" stroke="#0a4d9c" stroke-width="1.4"><path d="M1 1l4 4 4-4"/></svg></div>
<div class="abs lbl r" style="left:110px;width:132px;top:837px">FOB</div>
<div class="abs field select" style="left:262px;top:829px;width:160px"><span></span><svg class="chev" viewBox="0 0 10 6" fill="none" stroke="#0a4d9c" stroke-width="1.4"><path d="M1 1l4 4 4-4"/></svg></div>
<div class="abs lbl r" style="left:110px;width:132px;top:878px">Order Ship Rule</div>
<div class="abs field select" style="left:262px;top:868px;width:160px">Partials<svg class="chev" viewBox="0 0 10 6" fill="none" stroke="#0a4d9c" stroke-width="1.4"><path d="M1 1l4 4 4-4"/></svg></div>
<div class="abs lbl r" style="left:110px;width:132px;top:919px">Line Ship Rule</div>
<div class="abs field select" style="left:262px;top:908px;width:160px">Partials<svg class="chev" viewBox="0 0 10 6" fill="none" stroke="#0a4d9c" stroke-width="1.4"><path d="M1 1l4 4 4-4"/></svg></div>

<!-- shipping fields: middle column -->
<div class="abs lbl r" style="left:440px;width:109px;top:713px">Request Date</div>
<div class="abs field select" style="left:570px;top:706px;width:159px">01/07/2018
  <svg width="14" height="14" viewBox="0 0 14 14" fill="none" stroke="#0a4d9c" stroke-width="1.3"><rect x="1" y="2" width="12" height="11"/><path d="M1 5h12M4 0v3M10 0v3M4 7.5h1M6.5 7.5h1M9 7.5h1M4 10h1M6.5 10h1M9 10h1"/></svg></div>
<div class="abs lbl r" style="left:440px;width:109px;top:754px">Freight Terms</div>
<div class="abs field select" style="left:570px;top:747px;width:159px">Collected<svg class="chev" viewBox="0 0 10 6" fill="none" stroke="#0a4d9c" stroke-width="1.4"><path d="M1 1l4 4 4-4"/></svg></div>
<div class="abs lbl r" style="left:440px;width:109px;top:796px">Freight Calc</div>
<div class="abs field select" style="left:570px;top:788px;width:159px"><span></span><svg class="chev" viewBox="0 0 10 6" fill="none" stroke="#0a4d9c" stroke-width="1.4"><path d="M1 1l4 4 4-4"/></svg></div>

<!-- shipping fields: right column -->
<div class="abs lbl" style="left:756px;top:713px">Customer Ship To</div>
<div class="abs field" style="left:899px;top:706px;width:95px"></div>
<div class="abs lbl" style="left:1004px;top:712px;font-size:16px">/</div>
<div class="abs field" style="left:1019px;top:706px;width:40px"></div>

<div class="abs lock">
  <svg width="22" height="26" viewBox="0 0 22 26" fill="none" stroke="#84c441" stroke-width="2"><rect x="2" y="11" width="18" height="13" rx="1"/><path d="M6 11V7a5 5 0 0 1 10 0v4M11 15.5v4"/></svg>
</div>

<div class="abs hint">Enter property values, and click Apply</div>

</body>
</html>
```